Financial services firm needs updated web design

Our current website, corvelwealthgroup.example was created by ourselves using templates provided by our website host, Brightlane Hosting. We are looking to get a whole new look and feel to our website that is clean, professional and easy to navigate. The design must be able to be transferred to Brightlane Hosting for hosting (FTP??-outside my area of expertise - sorry) and that the information can be updated and changed by ourselves in the future. I have included our updated logo and our business card design.
Updates
Project Deadline Extended
Reason: Went away on vacation for two weeks.
Target Market(s)
Age 50+ individuals looking for investment, retirement and estate planning guidance.
Industry/Entity Type
Financial
Number of Pages Required
1 page
Font styles to use
Other font styles liked:
- Adobe Caslon Pro
Look and feel

```html
<!DOCTYPE html>
<html lang="en">
<head>
<meta charset="utf-8">
<title>Corvel Wealth Group</title>
<link rel="stylesheet" href="https://fonts.googleapis.com/css2?family=Open+Sans:wght@400;700&family=Roboto:wght@300;400&display=swap">
<style>
:root{
  --green:#4a9a4c;
  --green-dark:#2f7a33;
  --ink:#2e2e2e;
  --body:#555;
  --panel:#ffffff;
  --side:#e9e9e9;
  --side-light:#f0f0f0;
  --rule:#c9c9c9;
  --night:#0e0e0e;
}
*{margin:0;padding:0;box-sizing:border-box}
html,body{width:1142px;height:1200px;overflow:hidden;background:var(--night)}
body{position:relative;font-family:"Roboto",Arial,sans-serif;font-weight:300;color:var(--body)}
.hero-backdrop{position:absolute;left:0;top:0;width:1142px;height:700px;
  background:linear-gradient(180deg,#d9d2c2 0%,#c8c0ae 30%,#a59c8b 55%,#6a645b 78%,var(--night) 100%);}
.site-header{position:absolute;left:126px;top:27px;width:892px;height:67px;background:#fff;border-radius:3px;box-shadow:0 1px 4px rgba(0,0,0,.2)}
.brand{position:absolute;left:16px;top:16px;font-family:"Open Sans",sans-serif;font-size:30px;color:var(--green);display:flex;align-items:center;gap:10px;line-height:1}
.brand-mark{width:14px;height:14px;border-radius:50%;background:var(--green)}
.main-nav{position:absolute;right:18px;top:21px;display:flex;gap:4px;font-family:"Open Sans",sans-serif;font-size:14px;font-weight:400}
.main-nav a{color:#222;text-decoration:none;padding:3px 12px;border-radius:2px}
.main-nav a.active{background:var(--green);color:#fff}
.hero{position:absolute;left:0;top:170px;width:1142px;text-align:center;font-family:"Open Sans",sans-serif;color:#2a2a2a}
.hero-kicker{font-size:30px;font-weight:400}
.hero-title{font-size:39px;font-weight:700;line-height:48px;margin-top:10px;text-shadow:0 1px 2px rgba(255,255,255,.4)}
.quote-button{position:absolute;left:404px;top:348px;width:338px;height:66px;background:linear-gradient(#4f9a4f,var(--green-dark));border:1px solid #2b6a2e;border-radius:2px;color:#fff;font-family:"Open Sans",sans-serif;font-size:39px;line-height:62px;text-align:center;box-shadow:0 2px 4px rgba(0,0,0,.3);z-index:2}
.content-panel{position:absolute;left:126px;top:500px;width:892px;height:583px;background:var(--panel);border-radius:3px;overflow:hidden}
.sidebar{position:absolute;left:0;top:0;width:266px;height:583px;background:var(--side-light)}
.sidebar-services{height:336px;background:var(--side);padding:22px 13px 0}
.sidebar-news{padding:18px 13px 0}
.section-title{font-family:"Open Sans",sans-serif;font-weight:400;color:var(--ink);font-size:24px;line-height:30px}
.section-title em{font-style:normal;color:var(--green)}
.sidebar .section-title{border-bottom:1px solid var(--green);width:241px}
.service-list{list-style:none;width:241px;margin-top:4px}
.service-list li{font-size:15px;color:#333;height:29px;line-height:29px;border-bottom:1px dashed var(--rule);padding-left:4px}
.service-list li:last-child{border-bottom:none}
.arrow{color:var(--green);font-size:11px;margin-right:5px}
.news-item{width:241px;font-size:13px;line-height:16.5px;color:#333;padding:12px 0 8px 4px;border-bottom:1px dashed var(--rule)}
.news-item:last-child{border-bottom:none}
.news-item .date{color:var(--green)}
.news-item .more{color:var(--green);display:block;padding-left:14px}
.main-column{position:absolute;left:292px;top:22px;width:580px}
.main-column .section-title{font-size:25px}
.lead{font-size:12.5px;line-height:19.3px;margin-top:4px}
.lead+.lead{margin-top:8px}
.dotted{border-top:1px dotted #999;margin:12px 0 0}
.advisers-title{font-family:"Open Sans",sans-serif;font-weight:400;font-size:17px;color:var(--ink);margin-top:14px}
.advisers-title em{font-style:normal;color:var(--green)}
.adviser{position:absolute;top:239px;width:300px}
.adviser .portrait{position:absolute;left:-4px;top:0;width:97px;height:97px;border-radius:50%;background:#e4e4e4}
.adviser .info{position:absolute;left:106px;top:4px;width:190px;font-size:13px;line-height:16.5px}
.adviser .name{font-size:17px;color:var(--ink);line-height:20px;font-weight:400}
.read-more{color:var(--green);display:block}
.rule-lower{position:absolute;left:0;top:365px;width:580px;border-top:1px dotted #999}
.contact{position:absolute;left:0;top:382px;width:215px;font-size:13px;color:#333}
.contact .section-title,.newsletter .section-title{font-size:18px;line-height:24px}
.contact-row{padding:4px 0;border-bottom:1px dotted #999;line-height:17px;white-space:nowrap}
.contact-row:last-child{border-bottom:none}
.contact-row p+p{margin-top:6px}
.contact-row svg{vertical-align:-2px;margin-right:4px}
.contact-row .label{color:var(--green)}
.indent{padding-left:16px}
.newsletter{position:absolute;left:238px;top:382px;width:342px;font-size:13px}
.email-field{margin-top:12px;height:40px;border:1px solid #ccc;border-radius:3px;background:#ececec;padding:0 9px;line-height:38px;color:#555}
.check-row{margin-top:12px;display:flex;align-items:center;gap:6px}
.check{width:13px;height:13px;border:1px solid #888;background:#fff}
.subscribe-button{display:inline-block;margin-top:11px;background:var(--green);color:#fff;font-weight:400;padding:4px 7px;border-radius:2px;border:1px solid var(--green-dark)}
.site-footer{position:absolute;left:0;top:1106px;width:1142px;text-align:center;color:#eee;font-size:15px}
.site-footer .rule{width:646px;margin:7px auto 6px;border-top:1px solid #555}
.footer-links{font-size:13.5px;line-height:17px}
</style>
</head>
<body>
<div class="hero-backdrop" role="img" aria-label="Hazy photograph of a city skyline with skyscrapers fading into darkness"></div>

<header class="site-header">
  <div class="brand"><span class="brand-mark"></span>Corvel Wealth Group</div>
  <nav class="main-nav">
    <a class="active">Home</a><a>About Us</a><a>Our Services</a><a>News</a><a>Links</a><a>Contack Us</a>
  </nav>
</header>

<section class="hero">
  <p class="hero-kicker">We are Canada Based Financial Company</p>
  <h1 class="hero-title">Lorem Ipsum is simply dummy<br>text of the printing and typesetting industry.</h1>
</section>
<a class="quote-button">Get a Quote</a>

<main class="content-panel">
  <aside class="sidebar">
    <div class="sidebar-services">
      <h2 class="section-title">Our <em>Services</em></h2>
      <ul class="service-list">
        <li><span class="arrow">➔</span>Term Deposit Rates</li>
        <li><span class="arrow">➔</span>Income for Life</li>
        <li><span class="arrow">➔</span>NEW - 2012 Planning Tips</li>
        <li><span class="arrow">➔</span>Tax PlanningPlanning Tips</li>
        <li><span class="arrow">➔</span>Calculators</li>
        <li><span class="arrow">➔</span>Canadian Mortgage</li>
        <li><span class="arrow">➔</span>Financial Products</li>
        <li><span class="arrow">➔</span>Mutual Funds</li>
        <li><span class="arrow">➔</span>Disclosure Notices</li>
      </ul>
    </div>
    <div class="sidebar-news">
      <h2 class="section-title">Latest <em>News</em></h2>
      <div class="news-item"><span class="arrow">➔</span><span class="date">22-10-2014:</span> Lorem Ipsum is simply<br>dummy text of the printing and<br>typesetting industry.<span class="more">Read More</span></div>
      <div class="news-item"><span class="arrow">➔</span><span class="date">21-10-2014:</span> Lorem Ipsum is simply<br>dummy text of the printing and<br>typesetting industry.<span class="more">Read More</span></div>
    </div>
  </aside>

  <section class="main-column">
    <h2 class="section-title">Welcome to our <em>Website</em></h2>
    <p class="lead">Lorem Ipsum is simply dummy text of the printing and typesetting industry. Lorem Ipsum has been the industry's standard dummy text ever since the 1500s, when an unknown printer took a galley of type and scrambled it to make a type specimen book. It has survived not only five centuries, but also the leap into electronic typesetting, remaining essentially unchanged.</p>
    <p class="lead">It was popularised in the 1960s with the release of Letraset sheets containing Lorem Ipsum passages, and more recently with desktop publishing software like Aldus PageMaker including versions of Lorem Ipsum.</p>
    <div class="dotted"></div>
    <h3 class="advisers-title">Our <em>Finance Advisers</em></h3>

    <div class="adviser" style="left:0">
      <div class="portrait" role="img" aria-label="Illustrated portrait of adviser Everett D. Lawson"></div>
      <div class="info">
        <p class="name">Everett D. Lawson,<br>CFP, CLU, CHFC</p>
        He established his first financial services practice in 1981.
        <span class="read-more">Read More</span>
      </div>
    </div>
    <div class="adviser" style="left:300px">
      <div class="portrait" role="img" aria-label="Illustrated portrait of adviser Malcolm R. Lawson"></div>
      <div class="info">
        <p class="name">Malcolm R. Lawson, CFP</p>
        Malcolm Lawson is a Certified Financial Planner who has been working with Everett D. Lawson since 1997.
        <span class="read-more">Read More</span>
      </div>
    </div>

    <div class="rule-lower"></div>

    <div class="contact">
      <h3 class="section-title">Contact <em>Us</em></h3>
      <div class="contact-row"><svg width="12" height="9" viewBox="0 0 12 9"><rect width="12" height="9" fill="#4a9a4c"/><path d="M0 0l6 5 6-5" stroke="#fff" fill="none"/></svg>2280 Harbour Lane, Delta,<br><span class="indent">British Columbia, V0X 1Z0</span></div>
      <div class="contact-row"><p><span class="label">T:</span> (555)010-0144</p><p><span class="label">F:</span> (555)010-0147</p></div>
      <div class="contact-row"><p><svg width="12" height="12" viewBox="0 0 12 12"><circle cx="6" cy="6" r="5" stroke="#4a9a4c" fill="none"/><path d="M1 6h10M6 1v10" stroke="#4a9a4c"/></svg>elawson@corvelwg.example</p><p><svg width="12" height="12" viewBox="0 0 12 12"><circle cx="6" cy="6" r="5" stroke="#4a9a4c" fill="none"/><path d="M1 6h10M6 1v10" stroke="#4a9a4c"/></svg>mlawson@corvelwg.example</p></div>
    </div>

    <div class="newsletter">
      <h3 class="section-title">Subscribe to our <em>Newsletter!</em></h3>
      <p>And get latest updates, tips.</p>
      <div class="email-field">Enter Email...</div>
      <div class="check-row"><span class="check"></span>Subscribe for the monthly issues.</div>
      <a class="subscribe-button">Subscribe Now</a>
    </div>
  </section>
</main>

<footer class="site-footer">
  <p>©2007 - 2014 Corvel Wealth Group | All Rights Reserved</p>
  <div class="rule"></div>
  <p class="footer-links">Home | Everett D. Lawson, CFP | Malcolm R. Lawson, CFP | Interest Rates | Tax Tips | Planning Tips | Newsletter<br>Calculators | Financial Products | Links| Contact Us | Disclosure Notices</p>
</footer>
</body>
</html>
```